Church Bulletin Ad (see attached sample)

Create a New Church Bulletin Ad. I have attached some samples of what we would like to have in the ad. (1) Marrowfield Realty Quist Logo (2) Headshot (3) Lorna Tavish & Greta Tavish, Real Estate Team (4) Phone number (5) Email address (6) St Agathe Parishioners for over 40 Years. We would like for the ad to be clean and modern. NO OTHER IMAGES besides headshots and Marrowfield Realty Quist Logo.

Target Market(s)

Church community

Industry/Entity Type

Real Estate

Font styles to use
Sans Serif
Other font styles liked:
• Modern Font

Colors
0054AA
0677BA
7BADD7
CADEEF
E8F1F8

Requirements
Must have
• Marrowfield Realty Quist Logo; Headshot; Ad size is 4.5"x1.62"

```html
<!DOCTYPE html>
<html lang="en">
<head>
<meta charset="utf-8">
<title>Tavish Real Estate Team – Bulletin Ad</title>
<link rel="stylesheet" href="https://fonts.googleapis.com/css2?family=Montserrat:wght@600;700&family=Philosopher:wght@400;700&display=swap">
<style>
  :root {
    --navy: #0d2a55;
    --cyan: #0e9cc7;
    --cyan-soft: #5fc0dd;
    --white: #ffffff;
    --photo-warm: #d9b7a4;
    --photo-cool: #c7ccd2;
  }
  html, body {
    margin: 0;
    padding: 0;
    overflow: hidden;
    background: var(--white);
  }
  .ad {
    position: relative;
    width: 1200px;
    height: 432px;
    overflow: hidden;
    background: var(--white);
  }
  .ad__wave {
    position: absolute;
    inset: 0;
  }
  .slogan {
    position: absolute;
    left: 41px;
    top: 30px;
    width: 501px;
    height: 59px;
    background: var(--cyan);
    color: var(--white);
    font-family: "Montserrat", sans-serif;
    font-weight: 700;
    font-size: 23px;
    letter-spacing: 0.2px;
    display: flex;
    align-items: center;
    justify-content: center;
  }
  .team-name {
    position: absolute;
    left: 41px;
    top: 105px;
    margin: 0;
    font-family: "Philosopher", sans-serif;
    font-weight: 400;
    font-size: 40px;
    color: var(--navy);
    line-height: 1;
  }
  .team-role {
    position: absolute;
    left: 41px;
    top: 150px;
    margin: 0;
    font-family: "Philosopher", sans-serif;
    font-size: 29px;
    color: var(--cyan);
    line-height: 1;
  }
  .contact {
    position: absolute;
    left: 41px;
    top: 200px;
    margin: 0;
    padding: 0;
    list-style: none;
    font-family: "Montserrat", sans-serif;
    font-weight: 600;
    font-size: 22px;
    color: var(--navy);
    line-height: 27px;
  }
  .contact li::before {
    content: "";
    display: inline-block;
    width: 6px;
    height: 6px;
    border-radius: 50%;
    background: var(--navy);
    margin-right: 5px;
    vertical-align: middle;
  }
  .brand {
    position: absolute;
    left: 85px;
    top: 274px;
    width: 143px;
    height: 129px;
    box-sizing: border-box;
    border: 4px solid var(--white);
    background: var(--navy);
    color: var(--white);
    font-family: "Montserrat", sans-serif;
    font-weight: 600;
    font-size: 17px;
    line-height: 1.25;
    text-align: center;
    display: flex;
    align-items: center;
    justify-content: center;
    padding: 10px;
  }
  .headshot {
    position: absolute;
    border-radius: 50%;
    box-sizing: border-box;
    border: 9px solid var(--cyan);
    background: var(--white);
    padding: 4px;
  }
  .headshot__photo {
    width: 100%;
    height: 100%;
    border-radius: 50%;
  }
  .headshot--first {
    left: 582px;
    top: 40px;
    width: 284px;
    height: 284px;
  }
  .headshot--first .headshot__photo {
    background: radial-gradient(circle at 50% 45%, var(--photo-warm), #6b4636 75%);
  }
  .headshot--second {
    left: 901px;
    top: 10px;
    width: 266px;
    height: 266px;
  }
  .headshot--second .headshot__photo {
    background: radial-gradient(circle at 50% 45%, #e8d4cc, var(--photo-cool) 60%, #4a4140 90%);
  }
  .tagline {
    position: absolute;
    left: 271px;
    top: 364px;
    margin: 0;
    font-family: "Philosopher", sans-serif;
    font-size: 40px;
    color: var(--white);
    line-height: 1;
    white-space: nowrap;
  }
  .tagline__accent {
    color: var(--cyan);
  }
</style>
</head>
<body>
  <div class="ad">
    <svg class="ad__wave" width="1200" height="432" viewBox="0 0 1200 432" aria-hidden="true">
      <path d="M0 344 C 320 362, 760 352, 1200 248 L1200 432 L0 432 Z" fill="var(--cyan-soft)"/>
      <path d="M0 350 C 320 368, 760 358, 1200 256 L1200 432 L0 432 Z" fill="var(--navy)"/>
    </svg>

    <div class="slogan">ENERY EXCELLENCE EXPERIENCE</div>
    <h1 class="team-name">Lorna Tavish &amp; Greta Tavish</h1>
    <p class="team-role">Real Estate Team</p>
    <ul class="contact">
      <li>(206) 555-0148</li>
      <li>tavishteam@mrquist.com</li>
    </ul>

    <div class="brand">Marrowfield Realty Quist</div>

    <div class="headshot headshot--first">
      <div class="headshot__photo" role="img" aria-label="Headshot of Lorna Tavish"></div>
    </div>
    <div class="headshot headshot--second">
      <div class="headshot__photo" role="img" aria-label="Headshot of Greta Tavish"></div>
    </div>

    <p class="tagline">St Agathe Parishioners for over <span class="tagline__accent">40 Years</span></p>
  </div>
</body>
</html>
```